Simple fencing and steel manufacturing website

** update 01/04/2015 ** we did not add logo design, but if your font/logo is accepted we will add $50 to make it more fair
Even if you web design is not chosen, but your logo is, we will pay you $50. If both are chosen you will get an extra $50

Site map:
Home
About
Gallery
-photos
-testimonials
Contact

No current website:

No current logo, colors currently black and gold but we don't mind changing them - wide open brief
Happy for new font/style/logo for company name which is Railgate Supplies

Customer wants clean, credible and professional look & feel
stock photos OK

Brief:

One home page - simple with 2 or 3 small areas to tease and attract the user and one template page to suit all the other pages

All competitor websites are pretty bad, the best of them is
http://www.brelwynbarriers.com.au/index.html

Target Market(s)

Government and top level builders

Industry/Entity Type

Fencing

Requirements
Must have
• 1. Display ISO and environmental awards (ISO9001 AS4801 ISO14001)
• 2. A list of about 15 products
• Can be in teaser areas of home page as suggested before or slider or really anywhere
Nice to have
• Log with name - nice but not necessary (we don't have one)

```html
<!DOCTYPE html>
<html lang="en">
<head>
<meta charset="utf-8">
<title>Railgate Supplies</title>
<link href="https://fonts.googleapis.com/css2?family=Roboto:wght@300;400;500;700&display=swap" rel="stylesheet">
<style>
:root{
  --gold:#b5892f;
  --ink:#1a1a1a;
  --text:#333333;
  --panel:#e6e6e6;
  --page-bg:#ececf0;
  --white:#ffffff;
  --black:#000000;
  --line:#dcdcdc;
}
*{margin:0;padding:0;box-sizing:border-box}
html,body{width:1016px;height:1200px;overflow:hidden}
body{background:var(--page-bg);font-family:'Roboto',sans-serif;color:var(--text);position:relative}
.page{position:absolute;left:50px;top:0;width:916px;height:1200px;background:var(--white)}
.abs{position:absolute}

.brand{left:27px;top:22px;width:166px;display:flex;flex-direction:column;align-items:center}
.brand-mark{width:52px;height:52px;background:#1d4f73;margin-bottom:14px}
.brand-name{font-size:19px;font-weight:500;color:var(--ink);letter-spacing:.8px;white-space:nowrap}
.call{right:24px;top:34px;display:flex;align-items:center;gap:6px}
.call-label{font-size:11px;color:var(--ink)}
.call-number{font-size:17px;color:var(--ink);margin-left:6px}
.nav{left:604px;top:88px;display:flex;font-size:11px;font-weight:500;color:var(--ink)}
.nav a{color:inherit;text-decoration:none;height:26px;line-height:26px;padding:0 13px;margin-right:16px}
.nav a:last-child{margin-right:0}
.nav a.active{background:var(--gold);color:var(--white)}

.hero{left:0;top:137px;width:916px;height:434px;background:linear-gradient(180deg,#2f4a22 0%,#4b6b30 45%,#a9a79a 75%,#c9c4b8 100%)}
.hero-caption{left:78px;top:193px;width:316px;height:100px;background:rgba(40,40,40,.82);padding:18px 20px;color:var(--white)}
.hero-caption h2{font-size:16px;font-weight:500;margin-bottom:5px}
.hero-caption p{font-size:12px;font-weight:300;line-height:20px}
.dots{left:424px;top:392px;display:flex;gap:4px}
.dot{width:15px;height:15px;border-radius:50%;background:var(--white)}
.dot.on{background:radial-gradient(circle,#d0141b 0 4px,var(--white) 5px)}

.products{left:11px;top:581px;width:205px;height:419px;background:var(--panel)}
.products h3{background:var(--black);color:var(--white);font-size:12px;font-weight:500;height:37px;line-height:37px;padding-left:17px}
.products ul{list-style:none;padding:14px 0 0 20px}
.products li{font-size:11px;height:23.4px;line-height:23px;color:var(--text)}
.products li::before{content:"»";margin-right:10px;color:var(--ink)}

.main{left:243px;top:594px;width:404px}
.main h3{font-size:12px;font-weight:500;color:var(--gold);margin-bottom:13px}
.lead{font-size:11px;color:var(--ink);line-height:18.6px;margin-bottom:13px}
.body-text{font-size:11px;font-weight:300;line-height:18.6px;color:var(--text)}
.more{font-size:11px;font-weight:500;color:var(--gold);margin-top:13px;display:block}
.rule{border-top:1px solid var(--line);margin:17px 0 26px}

.location{left:688px;top:586px;width:216px;height:359px;border:1px solid var(--line);padding-top:22px}
.location h3{text-align:center;font-size:12px;font-weight:500;color:var(--gold)}
.map{position:absolute;left:21px;top:72px;width:176px;height:86px;background:radial-gradient(ellipse at center,#a9a9a9 0%,#c4c4c4 60%,#f2f2f2 100%)}
.info{position:absolute;left:30px;display:flex;gap:14px;font-size:11px;font-weight:300;color:var(--ink);line-height:21px}
.info svg{flex:none;margin-top:3px}

.footer{left:0;top:1015px;width:916px;height:185px;background:var(--black);color:var(--white)}
.footer h4{font-size:10px;font-weight:400;letter-spacing:.3px}
.social{display:flex;gap:6px;margin-top:14px}
.social span{width:27px;height:27px;border-radius:50%;background:var(--white)}
.badges{display:flex;gap:5px;margin-top:13px}
.badge{height:58px;background:var(--white)}
.foot-rule{left:0;top:134px;width:916px;border-top:1px solid #222}
.foot-links{left:23px;top:154px;font-size:9px;letter-spacing:.3px}
.foot-links span{margin:0 9px}
.copy{right:23px;top:154px;font-size:9px;letter-spacing:.3px}
</style>
</head>
<body>
<div class="page">
  <header>
    <div class="abs brand"><div class="brand-mark"></div><div class="brand-name">Railgate Supplies</div></div>
    <div class="abs call">
      <svg width="11" height="11" viewBox="0 0 24 24"><path fill="#1a1a1a" d="M6.6 10.8a15.1 15.1 0 006.6 6.6l2.2-2.2c.3-.3.7-.4 1-.2 1.1.4 2.3.6 3.6.6.6 0 1 .4 1 1V20c0 .6-.4 1-1 1A17 17 0 013 4c0-.6.4-1 1-1h3.5c.6 0 1 .4 1 1 0 1.3.2 2.5.6 3.6.1.3 0 .7-.2 1z"/></svg>
      <span class="call-label">Tell Us</span><span class="call-number">(02) 9417 2260</span>
    </div>
    <nav class="abs nav"><a class="active">HOME</a><a>ABOUT</a><a>GALLERY</a><a>CONTACT</a></nav>
  </header>

  <section class="abs hero" role="img" aria-label="Photo of a white ornamental sliding gate in front of palm trees and tropical garden">
    <div class="abs hero-caption">
      <h2>SLIDING GATE</h2>
      <p>Lorem Ipsum is simply dummy text of the printing and typesetting industry</p>
    </div>
    <div class="abs dots"><span class="dot"></span><span class="dot on"></span><span class="dot"></span><span class="dot"></span></div>
  </section>

  <aside class="abs products">
    <h3>OUR PRODUCTS</h3>
    <ul>
      <li>RTA Pedestrian (Type 1 - 5)</li><li>Partitions</li><li>Sporting Enclosures</li><li>Tubular (Pool/Garden)</li><li>Gates (Hinged)</li><li>Gates (Sliding)</li><li>Boom Gates</li><li>Turnstiles</li><li>Bollards</li><li>Wheelstops</li><li>Handrails</li><li>Guardrail</li><li>Privacy Screens</li><li>Steel Sheeting</li><li>Glass</li>
    </ul>
  </aside>

  <main class="abs main">
    <h3>WELCOME TO OUR SITE</h3>
    <p class="lead">There are many variations of passages of Lorem Ipsum available, but the majority have suffered alteration in some form</p>
    <p class="body-text">There are many variations of passages of Lorem Ipsum available, but the majority have suffered alteration in some form, by injected humour, or randomised words which don't look even slightly believable. If you are going to use a passage of Lorem Ipsum, you need to be sure there isn't anything embarrassing hidden in the middle of text. All the Lorem Ipsum generators on the Internet tend to repeat predefined<br>chunks.</p>
    <span class="more">Read More &rsaquo;</span>
    <div class="rule"></div>
    <h3>ABOUT US</h3>
    <p class="body-text">There are many variations of passages of Lorem Ipsum available, but the majority have suffered alteration in some form, by injected humour, or randomised words which don't look even slightly believable. If you are going to use a passage of Lorem Ipsum, you need to be sure there isn't anything embarrassing hidden in.</p>
    <span class="more" style="margin-top:14px">Read More &rsaquo;</span>
  </main>

  <aside class="abs location">
    <h3>OUR LOCATION</h3>
    <div class="map" role="img" aria-label="Grey world map"></div>
    <div class="info" style="top:198px">
      <svg width="12" height="15" viewBox="0 0 12 16"><path fill="#9a9a9a" d="M6 0a6 6 0 00-6 6c0 4.5 6 10 6 10s6-5.5 6-10a6 6 0 00-6-6zm0 8.5A2.5 2.5 0 116 3.5a2.5 2.5 0 010 5z"/></svg>
      <div>48 Tanner Street<br>Marlow, NSW 2790</div>
    </div>
    <div class="info" style="top:259px">
      <svg width="13" height="13" viewBox="0 0 24 24"><path fill="#9a9a9a" d="M6.6 10.8a15.1 15.1 0 006.6 6.6l2.2-2.2c.3-.3.7-.4 1-.2 1.1.4 2.3.6 3.6.6.6 0 1 .4 1 1V20c0 .6-.4 1-1 1A17 17 0 013 4c0-.6.4-1 1-1h3.5c.6 0 1 .4 1 1 0 1.3.2 2.5.6 3.6.1.3 0 .7-.2 1z"/></svg>
      <div>(02) 9417 2260</div>
    </div>
    <div class="info" style="top:302px">
      <svg width="14" height="11" viewBox="0 0 14 11"><rect x=".5" y=".5" width="13" height="10" fill="none" stroke="#9a9a9a"/><path d="M.5 .5L7 6l6.5-5.5" fill="none" stroke="#9a9a9a"/></svg>
      <div>info@railgatesupplies.com</div>
    </div>
  </aside>

  <footer class="abs footer">
    <div class="abs" style="left:25px;top:28px">
      <h4>CONNECT WITH US</h4>
      <div class="social"><span></span><span></span><span></span><span></span></div>
    </div>
    <div class="abs" style="left:647px;top:28px">
      <h4>OUR AWARDS</h4>
      <div class="badges"><span class="badge" style="width:132px"></span><span class="badge" style="width:48px;background:#f2c132"></span><span class="badge" style="width:59px"></span></div>
    </div>
    <div class="abs foot-rule"></div>
    <div class="abs foot-links">HOME<span>|</span>ABOUT<span>|</span>GALLERY<span>|</span>CONTACT</div>
    <div class="abs copy">COPYRIGHTS @ 2015 ALL RIGHTS RESERVED</div>
  </footer>
</div>
</body>
</html>
```